Need a image for a Chirpline ad campaign

Need a image designed for a Chirpline ad campaign. We are setting up a Chirpline campaign advertising on Chirpline for people who would want to get into modelling. We accept people aged 4+ . We want them to go to stepuptoposing dot com to sign up and apply. We need this image to comply with Chirpline ad policies. It can't have more than 20% text on it.

Maybe just say Become a Model or something
Step Up to Posing or something your choice.

What size should my ad image be?

The best image size to use for your ad depends on what type of ad you're creating, but a best practice is to size your images to be 1200 x 628 pixels. The Promo Format Manual contains all of the specifications around the recommended ad image sizes for each ad type. If your image is larger or smaller than the dimensions specified in the Promo Format Manual, it will be automatically resized to fit in the ad. Animated or flash images aren't supported.

Keep in mind that your ad may not contain more than 20% text in the ad's image.

Target Market(s)

People who would want to get into modelling

Industry/Entity Type

Advertising

Font styles to use
Sans Serif

Colors

Designer to choose colors to be used in the design.

Requirements
Must have
• Must tie in with the main website stepuptoposing dot com

```html
<!DOCTYPE html>
<html lang="en">
<head>
<meta charset="utf-8">
<title>Step Up to Posing – Platform for Aspiring Models</title>
<link rel="stylesheet" href="https://fonts.googleapis.com/css2?family=Bodoni+Moda:wght@400;500&display=swap">
<style>
  :root {
    --ink-deep: #141210;
    --ink-mid: #2c2722;
    --sepia-warm: #5a4b3d;
    --sepia-light: #8a7765;
    --lens-red: #7a2a14;
    --figure-glow: #f4f2ef;
    --figure-shade: #b9b5b0;
    --type-light: #f3f0ec;
    --rule-dots: rgba(220, 212, 200, 0.55);
  }

  html, body {
    margin: 0;
    padding: 0;
    overflow: hidden;
    background: var(--ink-deep);
  }

  .ad-canvas {
    position: relative;
    width: 1200px;
    height: 628px;
    overflow: hidden;
    background: var(--ink-deep);
  }

  .backdrop-photo {
    position: absolute;
    inset: 0;
    background:
      radial-gradient(ellipse 260px 240px at 860px 300px, rgba(122, 42, 20, 0.55) 0%, rgba(40, 30, 24, 0.0) 70%),
      radial-gradient(ellipse 520px 420px at 900px 260px, var(--sepia-warm) 0%, rgba(60, 50, 42, 0.4) 55%, rgba(20, 18, 16, 0) 85%),
      radial-gradient(ellipse 420px 260px at 1100px 80px, var(--sepia-light) 0%, rgba(138, 119, 101, 0) 70%),
      linear-gradient(100deg, var(--ink-deep) 0%, var(--ink-mid) 35%, #3a322b 60%, var(--ink-mid) 100%);
  }

  .model-photo {
    position: absolute;
    left: 0;
    top: 30px;
    width: 270px;
    height: 598px;
    background:
      radial-gradient(ellipse 110px 270px at 130px 320px, var(--figure-glow) 0%, #e3e0dc 55%, rgba(185, 181, 176, 0.6) 80%, rgba(185, 181, 176, 0) 100%);
    filter: blur(2px);
  }

  .headline-block {
    position: absolute;
    left: 350px;
    top: 130px;
    width: 700px;
    text-align: center;
    color: var(--type-light);
    font-family: "Bodoni Moda", "Didot", serif;
  }

  .dotted-rule {
    height: 0;
    border-top: 2px dotted var(--rule-dots);
    margin: 0;
  }

  .headline {
    margin: 0;
    font-weight: 400;
    line-height: 1;
    text-shadow: 0 2px 8px rgba(0, 0, 0, 0.5);
  }

  .headline-line {
    display: block;
  }

  .headline-line--large {
    font-size: 104px;
    letter-spacing: 2px;
  }

  .headline-line--top {
    margin-top: 42px;
  }

  .headline-line--small {
    font-size: 44px;
    letter-spacing: 1px;
    margin: 26px 0 22px;
  }

  .headline-line--bottom {
    margin-bottom: 26px;
  }

  .tagline {
    margin: 36px 0 0;
    font-size: 15px;
    letter-spacing: 7.4px;
    font-weight: 400;
    color: var(--type-light);
  }
</style>
</head>
<body>
  <main class="ad-canvas">
    <div class="backdrop-photo" role="img" aria-label="Sepia close-up of a vintage film camera lens resting on dark fabric"></div>
    <div class="model-photo" role="img" aria-label="Monochrome photo of a blonde model posing in a fitted white dress with a soft white glow"></div>

    <section class="headline-block">
      <hr class="dotted-rule">
      <h1 class="headline">
        <span class="headline-line headline-line--large headline-line--top">STEP</span>
        <span class="headline-line headline-line--small">UP TO</span>
        <span class="headline-line headline-line--large headline-line--bottom">POSING</span>
      </h1>
      <hr class="dotted-rule">
      <p class="tagline">PLATFORM FOR ASPIRING MODELS</p>
    </section>
  </main>
</body>
</html>
```